Orrowind Partners Business Card

Looking for a design for our business cards. Need to look corporate and outstanding. I have enclosed our logos for the company. Orrowind partners is an investment firm for high level clients looking for advisory in their investments. White background or black is good. We will like to double sided options maybe at the back with just the logo of the firm.

Example of the info for the business card:

Edric Salvo
Managing Director

Panama Phone +507 384 7165
Switzerland Phone +41 44 917 2638
mail@orrowind-partners.example
www.orrowind-partners.example

Industry/Entity Type

Investment

```html
<!DOCTYPE html>
<html lang="en">
<head>
<meta charset="utf-8">
<title>Orrowind Partners Business Card</title>
<link rel="stylesheet" href="https://fonts.googleapis.com/css2?family=Marcellus&display=swap">
<style>
  :root {
    --navy: #27387f;
    --navy-band: #3b4f97;
    --gold: #b18a2e;
    --band-grey: #d6d7d9;
    --ink: #2b2b2b;
    --muted: #6b6b6b;
    --card: #ffffff;
    --stage: #1c1c1c;
  }
  * { margin: 0; padding: 0; box-sizing: border-box; }
  html, body { width: 1200px; height: 1000px; overflow: hidden; }
  body {
    background: var(--stage);
    font-family: "Marcellus", "Optima", serif;
    position: relative;
  }
  .card {
    position: absolute;
    top: 345px;
    width: 540px;
    height: 310px;
    background: var(--card);
    overflow: hidden;
  }
  .card--front { left: 40px; }
  .card--back { left: 620px; }
  .card__bands { position: absolute; inset: 0; }
  .brand {
    position: absolute;
    display: flex;
    align-items: center;
    gap: 14px;
    color: var(--navy);
    text-transform: uppercase;
    letter-spacing: 0.12em;
  }
  .brand__mark { background: var(--navy); flex: none; }
  .card--front .brand { left: 120px; top: 52px; font-size: 26px; }
  .card--front .brand__mark { width: 22px; height: 22px; }
  .card--back .brand { left: 100px; top: 70px; font-size: 30px; }
  .card--back .brand__mark { width: 26px; height: 26px; }
  .holder { position: absolute; left: 36px; top: 124px; }
  .holder__name { color: var(--navy); font-size: 18px; letter-spacing: 0.04em; }
  .holder__role { color: var(--muted); font-size: 12px; margin-top: 2px; }
  .contact { position: absolute; left: 36px; top: 190px; font-size: 12px; line-height: 1.55; color: var(--ink); }
  .contact__label { color: var(--gold); font-variant: small-caps; letter-spacing: 0.04em; margin-left: 8px; }
  .contact__email { text-transform: uppercase; font-size: 11px; }
  .web {
    position: absolute;
    color: #fff;
    font-size: 13px;
    letter-spacing: 0.06em;
    text-transform: uppercase;
  }
  .card--front .web { left: 330px; top: 212px; }
  .card--back .web { left: 60px; top: 185px; color: var(--muted); }
</style>
</head>
<body>
  <section class="card card--front">
    <svg class="card__bands" width="540" height="310" viewBox="0 0 540 310" aria-hidden="true">
      <rect x="0" y="115" width="360" height="55" fill="var(--band-grey)"/>
      <polygon points="300,170 360,170 330,200 270,200" fill="var(--gold)"/>
      <polygon points="360,170 540,170 540,245 285,245 330,200" fill="var(--navy-band)"/>
      <polygon points="360,115 400,115 360,170" fill="var(--band-grey)"/>
    </svg>
    <div class="brand"><span class="brand__mark"></span>Orrowind Partners</div>
    <div class="holder">
      <p class="holder__name">Edric Salvo</p>
      <p class="holder__role">Managing Director</p>
    </div>
    <div class="contact">
      <p>+507 384 7165<span class="contact__label">Panama Phone</span></p>
      <p>+41 44 917 2638<span class="contact__label">Switzerland Phone</span></p>
      <p class="contact__email">mail@orrowind-partners.example</p>
    </div>
    <p class="web">www.orrowind-partners.example</p>
  </section>

  <section class="card card--back">
    <svg class="card__bands" width="540" height="310" viewBox="0 0 540 310" aria-hidden="true">
      <rect x="0" y="170" width="400" height="45" fill="var(--band-grey)"/>
      <polygon points="400,170 540,170 540,215 370,215" fill="var(--band-grey)"/>
      <polygon points="390,215 430,215 410,250 370,250" fill="var(--gold)"/>
      <polygon points="430,215 540,215 540,250 410,250" fill="var(--navy-band)"/>
    </svg>
    <div class="brand"><span class="brand__mark"></span>Orrowind Partners</div>
    <p class="web">www.orrowind-partners.example</p>
  </section>
</body>
</html>
```